Health Care Company with Logo Needs Business Cards designed

We are a luxury behavioral health company looking for business cards design we already have a logo and are looking for someone to design a sophisticated luxurious looking business card. Please note that Card design should be captivating just like the logo and also encompass the logo color

Industry/Entity Type

Healthcare

Contact Information for Business Card

Logo,company name, tagline, my name and title, contact details, and physical address

```html
<!DOCTYPE html>
<html lang="en">
<head>
<meta charset="utf-8">
<title>Orin Behavioral Health – Business Card</title>
<link rel="stylesheet" href="https://fonts.googleapis.com/css2?family=Arimo:wght@400;700&display=swap">
<style>
  :root {
    --page-bg: #e6e3de;
    --card-light: #f1e8d8;
    --card-mid: #ddd0bb;
    --card-warm: #c7b293;
    --brand-purple: #5b2380;
    --brand-blue: #1a86c4;
    --name-teal: #137f9c;
    --ink: #2b2a28;
    --purple-deep: #32123a;
    --purple-bright: #6a2f8e;
    --band-teal: #0b5f72;
    --band-green: #5f9e24;
    --contact-ink: #ece6ee;
  }
  * { margin: 0; padding: 0; box-sizing: border-box; }
  html, body {
    width: 1200px; height: 927px; overflow: hidden;
    background: var(--page-bg);
  }
  .business-card {
    position: absolute; left: 50px; top: 156px;
    width: 1100px; height: 614px; overflow: hidden;
    background: linear-gradient(100deg, var(--card-light) 0%, var(--card-mid) 45%, var(--card-warm) 80%, var(--card-mid) 100%);
    box-shadow: 0 10px 30px rgba(0,0,0,0.18);
    font-family: "Arimo", Arial, sans-serif;
  }
  .decor-band {
    position: absolute; left: 0; right: 0; top: 420px; bottom: 0;
    background: linear-gradient(90deg, var(--band-teal) 0%, var(--purple-deep) 35%, var(--purple-bright) 72%, var(--purple-deep) 100%);
    border-top: 8px solid var(--band-green);
  }
  .brand { position: absolute; left: 68px; top: 68px; display: flex; align-items: flex-start; gap: 18px; }
  .brand-square { width: 62px; height: 62px; background: var(--brand-purple); margin-top: 2px; }
  .brand-name {
    font-weight: 700; font-size: 38px; line-height: 1.1; color: var(--brand-purple);
  }
  .brand-tagline {
    font-weight: 700; font-size: 12px; letter-spacing: 2px; color: var(--brand-blue);
    margin-top: 8px; text-transform: uppercase;
  }
  .holder { position: absolute; right: 57px; top: 68px; text-align: right; }
  .holder-name { font-weight: 700; font-size: 38px; color: var(--name-teal); line-height: 1.1; }
  .holder-title { font-size: 28px; color: var(--ink); margin-top: 6px; }
  .address { position: absolute; left: 68px; top: 296px; font-size: 28px; line-height: 38px; color: var(--ink); }
  .contact { position: absolute; right: 57px; top: 456px; list-style: none; }
  .contact li {
    display: flex; justify-content: flex-end; align-items: center; gap: 14px;
    font-size: 27px; line-height: 38px; color: var(--contact-ink);
  }
  .contact svg { width: 24px; height: 24px; flex: none; }
</style>
</head>
<body>
  <div class="business-card">
    <div class="decor-band" role="img" aria-label="Decorative flowing band in the brand's green, teal and purple tones"></div>

    <div class="brand">
      <div class="brand-square"></div>
      <div>
        <div class="brand-name">Orin Behavioral Health</div>
        <div class="brand-tagline">Guiding minds toward calm and lasting wellness</div>
      </div>
    </div>

    <div class="holder">
      <div class="holder-name">Daniel Reyes</div>
      <div class="holder-title">Manager</div>
    </div>

    <p class="address">Your address, city<br>state, ZIP 0000</p>

    <ul class="contact">
      <li>123-456-2100
        <svg viewBox="0 0 24 24" fill="var(--contact-ink)" aria-hidden="true"><path d="M6.6 10.8c1.4 2.8 3.8 5.2 6.6 6.6l2.2-2.2c.3-.3.7-.4 1-.2 1.1.4 2.3.6 3.6.6.6 0 1 .4 1 1V20c0 .6-.4 1-1 1C10.6 21 3 13.4 3 4c0-.6.4-1 1-1h3.5c.6 0 1 .4 1 1 0 1.3.2 2.5.6 3.6.1.3 0 .7-.2 1z"/></svg>
      </li>
      <li>youremail@mailbox.com
        <svg viewBox="0 0 24 24" fill="none" stroke="var(--contact-ink)" stroke-width="1.8" aria-hidden="true"><rect x="3" y="5" width="18" height="14" rx="2"/><path d="M3 7l9 6 9-6"/></svg>
      </li>
      <li>www.yourwebsite.com
        <svg viewBox="0 0 24 24" fill="none" stroke="var(--contact-ink)" stroke-width="1.6" aria-hidden="true"><circle cx="12" cy="12" r="9"/><path d="M3 12h18M12 3c3 3 3 15 0 18M12 3c-3 3-3 15 0 18M4.5 7.5h15M4.5 16.5h15"/></svg>
      </li>
    </ul>
  </div>
</body>
</html>
```